LoanHarbor
I need double sided standard sized Business Card [3.5" x 2"]
Select font that compliments logo font
Simple
Pawel Merrin
Vice President - Purchase Division
4718 Birchwood Lane, Suite 300
Costa Mesa, CA 92681
Toll 800.517.2094
Direct 714.390.8152
Cell 949.306.7428
EFax 877.614.9087
pawelmerrin@loanharbor-example.net
www.loanharbor-example.net
NMLS# 748159
use periods in phone numbers instead of dashes. I like clean, aligned information and a lot of "negative" space. I want 2 versions one for the white background on white card, and one for the black background on a black card. Black card will be white on flip side.
This side is in the works. Will post very soon. Verbage.for both cards will be the same.

```html
<!DOCTYPE html>
<html lang="en">
<head>
<meta charset="utf-8">
<title>LoanHarbor Business Cards</title>
<link href="https://fonts.googleapis.com/css2?family=Open+Sans:wght@400;600;700&display=swap" rel="stylesheet">
<style>
  :root {
    --stage: #d9c3a5;
    --card-black: #0d0d0f;
    --card-white: #ffffff;
    --brand-blue: #2c8fd3;
    --brand-navy: #1f3550;
    --ink: #3a3f47;
    --muted: #8a9099;
    --on-dark: #f2f4f7;
  }
  * { box-sizing: border-box; margin: 0; padding: 0; }
  html, body {
    width: 1200px; height: 646px; overflow: hidden;
    background: var(--stage);
    font-family: "Open Sans", Arial, sans-serif;
  }
  .stage {
    width: 1200px; height: 646px;
    display: flex; align-items: center; justify-content: center; gap: 56px;
  }
  .card {
    position: relative;
    width: 525px; height: 300px;
    border-radius: 4px;
    box-shadow: 0 8px 22px rgba(0,0,0,.22);
    overflow: hidden;
  }

  /* Black side */
  .card--back { background: var(--card-black); color: var(--on-dark); }
  .back-brand {
    position: absolute; top: 112px; left: 0; right: 0;
    display: flex; align-items: center; justify-content: center; gap: 10px;
  }
  .brand-dot {
    width: 14px; height: 14px; border-radius: 50%;
    background: var(--brand-blue);
  }
  .back-brand .brand-name {
    font-size: 34px; font-weight: 600; color: var(--on-dark); letter-spacing: -.3px;
  }
  .back-license {
    position: absolute; top: 176px; left: 0; right: 0;
    text-align: center; font-size: 12px; color: var(--on-dark); letter-spacing: .3px;
  }

  /* White side */
  .card--front { background: var(--card-white); color: var(--ink); }
  .front-edge { position: absolute; inset: 0; }
  .front-brand {
    position: absolute; top: 34px; left: 40px;
    display: flex; align-items: center; gap: 9px;
  }
  .front-brand .brand-name {
    font-size: 30px; font-weight: 600; color: var(--brand-navy); letter-spacing: -.3px;
  }
  .holder {
    position: absolute; top: 40px; right: 36px; text-align: right;
  }
  .holder-name { font-size: 15px; font-weight: 700; color: var(--brand-blue); }
  .holder-title { font-size: 10.5px; color: var(--muted); margin-top: 3px; }

  .contact {
    position: absolute; top: 104px; left: 50px;
    list-style: none; font-size: 10.5px; line-height: 14.6px; color: var(--ink);
  }
  .contact li { display: flex; align-items: center; gap: 6px; }
  .contact .icon { width: 10px; height: 10px; flex: none; }
  .contact .spacer { width: 10px; flex: none; }
  .contact .gap { height: 5px; }
</style>
</head>
<body>
<main class="stage">

  <section class="card card--back" aria-label="Business card, black side">
    <div class="back-brand">
      <span class="brand-dot"></span>
      <span class="brand-name">LoanHarbor</span>
    </div>
    <p class="back-license">Lic no. NMLS# 748159</p>
  </section>

  <section class="card card--front" aria-label="Business card, white side">
    <svg class="front-edge" viewBox="0 0 525 300" width="525" height="300" aria-hidden="true">
      <path d="M0 0 H14 V250 Q14 282 46 284 H525 V300 H0 Z" fill="var(--brand-blue)"/>
      <path d="M20 90 V246 Q20 276 50 278 H525" fill="none" stroke="var(--brand-blue)" stroke-width="1" opacity=".35"/>
    </svg>

    <div class="front-brand">
      <span class="brand-dot"></span>
      <span class="brand-name">LoanHarbor</span>
    </div>

    <div class="holder">
      <p class="holder-name">Pawel Merrin</p>
      <p class="holder-title">Vice President - Purchase Division</p>
    </div>

    <ul class="contact">
      <li>
        <svg class="icon" viewBox="0 0 10 10"><path d="M5 0.5a3.2 3.2 0 0 0-3.2 3.2C1.8 6.2 5 9.5 5 9.5s3.2-3.3 3.2-5.8A3.2 3.2 0 0 0 5 .5z" fill="var(--brand-blue)"/><circle cx="5" cy="3.7" r="1.2" fill="#fff"/></svg>
        4718 Birchwood Lane, Suite 300
      </li>
      <li><span class="spacer"></span>Costa Mesa, CA 92681</li>
      <li><span class="spacer"></span>NMLS# 748159</li>
      <li class="gap"></li>
      <li>
        <svg class="icon" viewBox="0 0 10 10"><path d="M2.2 .8l1.6 2-1 1.1a6 6 0 0 0 3.3 3.3l1.1-1 2 1.6-.9 1.5C4.5 9.2.8 5.5 .7 1.7z" fill="var(--brand-blue)"/></svg>
        800.517.2094 (Toll)
      </li>
      <li>
        <svg class="icon" viewBox="0 0 10 10"><path d="M2.2 .8l1.6 2-1 1.1a6 6 0 0 0 3.3 3.3l1.1-1 2 1.6-.9 1.5C4.5 9.2.8 5.5 .7 1.7z" fill="var(--brand-blue)"/></svg>
        714.390.8152 (Direct)
      </li>
      <li>
        <svg class="icon" viewBox="0 0 10 10"><rect x="2.5" y=".5" width="5" height="9" rx="1" fill="var(--brand-blue)"/><rect x="3.4" y="1.6" width="3.2" height="5.6" fill="#fff"/></svg>
        949.306.7428 (Cell)
      </li>
      <li>
        <svg class="icon" viewBox="0 0 10 10"><rect x="1" y="3.5" width="8" height="5" rx=".8" fill="var(--brand-blue)"/><rect x="2.8" y="1" width="4.4" height="3" fill="var(--brand-blue)"/><rect x="3.4" y="5.6" width="3.2" height="1" fill="#fff"/></svg>
        877.614.9087 (EFax)
      </li>
      <li>
        <svg class="icon" viewBox="0 0 10 10"><rect x=".5" y="2" width="9" height="6.2" rx=".8" fill="var(--brand-blue)"/><path d="M1 2.5l4 3 4-3" fill="none" stroke="#fff" stroke-width=".9"/></svg>
        pawelmerrin@loanharbor-example.net
      </li>
      <li>
        <svg class="icon" viewBox="0 0 10 10"><circle cx="5" cy="5" r="4.3" fill="none" stroke="var(--brand-blue)" stroke-width="1"/><ellipse cx="5" cy="5" rx="1.8" ry="4.3" fill="none" stroke="var(--brand-blue)" stroke-width=".8"/><path d="M.8 5h8.4" stroke="var(--brand-blue)" stroke-width=".8"/></svg>
        www.loanharbor-example.net
      </li>
    </ul>
  </section>

</main>
</body>
</html>
```